Eye Institute Needs New Look

I have very detailed notes to guide you but be creative where needed. Attached are a screenshot of a wp theme i like and how i would like most content cut out and certain parts used. Site should be in blues.

Their current site is CLEARVALEOPTIC.com and you can pull some content and their logo from there (sorry, that is the best i can get from them for logo)

the theme I like is: http://brintor-sample.com/velmora_wp/

but review attached notes to see changes I want and direction of website.

All of the designs are VERY well done and followed instructions well.  They all are very similar and what I was looking for.  But all designers made two consistent mistakes.  For any that wish to be considered and still in the running for the final decision, I need these two changes to your submissions:

1) the designs are too clean / white.  I was looking for the content areas to be shades of blue , dark blue, etc so that the new site design isn't white and clean like their current site.

2) the boxes under the header.  I have seen versions with the grays and blues.  Can we try it with some bold multi colors for pop like red, yellow, green, orange, etc?

3) overall, this is an example site they liked http://www.mypeltonvision.com/ , can you get the site to have some splash of a bold complimentary highlight color and less overall white in the site?

Thank you and I look forward to submissions.  I need to show the client tomorrow so hopefully anyone still considering can get me revisions in the next 12 hours.

```html
<!DOCTYPE html>
<html lang="en">
<head>
<meta charset="utf-8">
<title>Clearvale Optic Institute</title>
<link href="https://fonts.googleapis.com/css2?family=Open+Sans:ital,wght@0,400;0,600;0,700;1,400&display=swap" rel="stylesheet">
<style>
:root{
  --brand:#0c4a80;
  --brand-deep:#082f55;
  --brand-mid:#11487c;
  --brand-light:#2a8fd8;
  --sky:#9fd0f5;
  --accent:#f5821f;
  --tile-red:#d63a2f;
  --tile-yellow:#e9a514;
  --tile-green:#2f9a4c;
  --tile-orange:#ef6c1a;
  --ink:#333;
  --footer:#0a2440;
  --footer-head:#0f3258;
  --muted:#c9d7e6;
}
*{box-sizing:border-box;margin:0;padding:0}
html,body{width:881px;height:1200px;overflow:hidden;background:var(--brand-deep)}
body{font-family:"Open Sans",Arial,sans-serif;color:var(--ink);position:relative}
.abs{position:absolute}

/* header */
.site-header{position:absolute;left:0;top:0;width:881px;height:60px;background:#fff;border-bottom:3px solid var(--accent)}
.brand{left:116px;top:12px;line-height:1}
.brand-name{display:flex;align-items:center;gap:6px;font-weight:700;font-size:24px;color:var(--brand);letter-spacing:-0.5px}
.brand-dot{width:10px;height:10px;border-radius:50%;background:var(--brand)}
.brand-sub{font-size:11px;color:var(--brand);margin-top:3px;padding-left:16px}
.topbar{right:117px;top:10px;display:flex;align-items:center;gap:8px;font-size:10px;color:var(--brand)}
.topbar .sep{color:#888;margin:0 4px}
.social{width:13px;height:13px;background:#8aa3bd;border-radius:2px}
.main-nav{right:117px;top:31px;display:flex;font-size:10px;text-transform:uppercase}
.main-nav a{color:#222;text-decoration:none;padding:6px 9px;line-height:12px}
.main-nav a.active{background:var(--brand-light);color:#fff}

/* hero */
.hero{left:0;top:60px;width:881px;height:278px;background:linear-gradient(90deg,#bcd3e0 0%,#d6e5ee 40%,#c3d7e3 70%,#9fbdcf 100%)}
.hero-person{left:150px;top:60px;width:320px;height:278px;background:linear-gradient(180deg,#8a5a3c 0%,#c99a7c 35%,#e3bca5 60%,#d8e4ec 100%);opacity:.85}
.hero-copy{right:119px;top:127px;text-align:right;width:190px}
.hero-copy h1{font-size:22px;font-weight:600;color:var(--brand);letter-spacing:.2px}
.hero-copy h2{font-size:12px;font-weight:700;color:var(--brand);margin-top:12px}
.hero-copy p{font-size:11.5px;line-height:15.5px;color:#333;margin-top:2px}
.btn-solid{display:inline-block;background:var(--accent);color:#fff;font-size:11px;font-weight:600;padding:6px 11px;margin-top:11px}
.hero-dots{right:119px;top:274px;display:flex;gap:3px}
.hero-dots span{width:7px;height:7px;background:#8e9aa3}
.hero-dots span.on{background:var(--accent)}

/* appointment band */
.cta-band{left:0;top:338px;width:881px;height:46px;background:var(--brand)}
.cta-band p{position:absolute;left:116px;top:14px;color:#fff;font-style:italic;font-size:14px}
.btn-light{position:absolute;right:118px;top:11px;background:var(--accent);color:#fff;font-size:10.5px;font-weight:600;padding:5px 11px;border-radius:3px}

/* service tiles */
.services-band{left:0;top:384px;width:881px;height:234px;background:var(--brand-deep)}
.services{left:115px;top:405px;display:flex}
.tile{width:162px;height:192px;color:#fff;text-align:center;padding-top:22px}
.tile.cataracts{background:var(--tile-red)}
.tile.laser{background:var(--tile-yellow)}
.tile.glaucoma{background:var(--tile-green)}
.tile.shop{background:var(--tile-orange)}
.tile svg{height:28px;width:32px}
.tile h3{font-size:17px;font-weight:600;margin-top:6px}
.tile p{font-size:9.6px;line-height:13px;margin:6px 12px 0}
.tile .btn-outline{display:inline-block;border:2px solid rgba(255,255,255,.85);font-size:9.5px;padding:4px 8px;margin-top:12px}

/* info area */
.info{left:0;top:618px;width:881px;height:202px;background:var(--brand-mid)}
.info h2{font-size:14px;font-weight:400;color:var(--sky)}
.feature{position:absolute;left:116px;top:20px;width:296px}
.feature p{font-size:9.3px;line-height:13px;margin-top:12px;color:#e6eef6}
.feature .more{margin-top:24px}
.feature .more span{color:var(--accent)}
.appt{position:absolute;left:461px;top:20px;width:232px}
.appt form{margin-top:10px}
.field{height:21px;border:1px solid #7fa3c6;background:#fff;margin-top:5px;font-size:9.5px;padding:3px 6px;color:#444;position:relative}
.field .cal{position:absolute;right:2px;top:3px;width:14px;height:13px;background:#9ab;border-top:3px solid #556}
.types{font-size:9.5px;margin-top:9px;display:flex;gap:9px;align-items:center;color:#e6eef6}
.types i{display:inline-block;width:7px;height:7px;border:1px solid #cfe0ef;border-radius:50%;margin-right:3px}
.btn-submit{display:inline-block;background:var(--accent);color:#fff;font-size:11px;padding:4px 13px;margin-top:10px}

/* footer */
.footer{left:0;top:845px;width:881px;height:355px;background:var(--footer);color:var(--muted);font-size:9.2px}
.footer-heads{height:45px;background:var(--footer-head);border-top:3px solid var(--accent)}
.footer-heads h4{position:absolute;top:16px;font-size:12px;font-weight:400;color:#fff;text-transform:uppercase}
.col{position:absolute;top:60px;width:150px;line-height:13px}
.links li{list-style:none;border-bottom:1px dashed #4d6785;padding:0 0 6px;margin-bottom:7px}
.map{width:144px;height:112px;background:#123a63;margin-top:8px;position:relative}
.map div{position:absolute;left:30px;top:14px;width:84px;height:84px;background:#5a82c7;border-radius:30% 40% 20% 35%}
.phones{width:180px}
.phones p{margin-bottom:8px}
.footer-rule{position:absolute;left:116px;top:231px;width:648px;border-top:1px solid #2c4a6b}
.copyright{position:absolute;left:116px;top:249px;font-style:italic;font-size:8.6px}
.backtop{position:absolute;right:146px;top:249px;font-style:italic;font-size:8.6px}
.about{position:absolute;left:116px;top:274px;width:650px;font-style:italic;font-size:8.4px;line-height:13px}
</style>
</head>
<body>

<header class="site-header">
  <div class="abs brand">
    <div class="brand-name"><span class="brand-dot"></span>Clearvale</div>
    <div class="brand-sub">Optic Institute</div>
  </div>
  <div class="abs topbar">
    <svg width="10" height="10" viewBox="0 0 24 24"><path fill="#0c4a80" d="M6.6 10.8a15 15 0 0 0 6.6 6.6l2.2-2.2a1 1 0 0 1 1-.25 11 11 0 0 0 3.6.6 1 1 0 0 1 1 1V20a1 1 0 0 1-1 1A17 17 0 0 1 3 4a1 1 0 0 1 1-1h3.5a1 1 0 0 1 1 1c0 1.25.2 2.45.6 3.6a1 1 0 0 1-.25 1z"/></svg>
    <span>(555) 014-2270</span><span class="sep">|</span>
    <span class="social"></span><span class="social"></span>
  </div>
  <nav class="abs main-nav">
    <a class="active">Home</a><a>Our Practice</a><a>Services</a><a>Education</a><a>Locations</a><a>Contact</a>
  </nav>
</header>

<section class="abs hero" role="img" aria-label="Soft blue studio backdrop"></section>
<div class="abs hero-person" role="img" aria-label="Photo of a smiling patient wearing rimless glasses"></div>
<div class="abs hero-copy">
  <h1>LASIK SURGERY</h1>
  <h2>TRUSTED</h2>
  <p>Why are people trusting Clearvale Optic Institute for their eyecare?</p>
  <span class="btn-solid">Know More &gt;</span>
</div>
<div class="abs hero-dots"><span class="on"></span><span></span><span></span></div>

<section class="abs cta-band">
  <p>Make an appointment today at any of our convenient Michigan offices!</p>
  <span class="btn-light">LOCATIONS</span>
</section>

<div class="abs services-band"></div>
<section class="abs services">
  <article class="tile cataracts">
    <svg viewBox="0 0 32 28"><path d="M1 14C6 6 26 6 31 14 26 22 6 22 1 14z" fill="#fff"/><circle cx="16" cy="14" r="6" fill="#d63a2f"/><circle cx="17.5" cy="12.5" r="2" fill="#fff"/></svg>
    <h3>cataracts</h3>
    <p>Learn more about the risks of each, symptoms, treatments and how Clearvale Optic Institute can help you.</p>
    <span class="btn-outline">LEARN MORE</span>
  </article>
  <article class="tile laser">
    <svg viewBox="0 0 32 28"><circle cx="19" cy="10" r="7" fill="none" stroke="#fff" stroke-width="2.5"/><path d="M14 15 6 25" stroke="#fff" stroke-width="4" stroke-linecap="round"/></svg>
    <h3>laser</h3>
    <p>Learn more about the risks of each, symptoms, treatments and how Clearvale Optic Institute can help you.</p>
    <span class="btn-outline">LEARN MORE</span>
  </article>
  <article class="tile glaucoma">
    <svg viewBox="0 0 32 28"><circle cx="16" cy="14" r="9" fill="none" stroke="#fff" stroke-width="1.5"/><circle cx="16" cy="14" r="3" fill="#fff"/><path d="M16 1v9M16 18v9M3 14h9M20 14h9" stroke="#fff" stroke-width="1.5"/></svg>
    <h3>glaucoma</h3>
    <p>Learn more about the risks of each, symptoms, treatments and how Clearvale Optic Institute can help you.</p>
    <span class="btn-outline">LEARN MORE</span>
  </article>
  <article class="tile shop">
    <svg viewBox="0 0 32 28"><path d="M3 4h5l3 14h15l3-10H10" fill="none" stroke="#fff" stroke-width="2"/><path d="M12 11h15M13 14h13" stroke="#fff" stroke-width="1.5"/><circle cx="13" cy="23" r="2" fill="#fff"/><circle cx="24" cy="23" r="2" fill="#fff"/></svg>
    <h3>eye shop</h3>
    <p>Learn more about the risks of each, symptoms, treatments and how Clearvale Optic Institute can help you.</p>
    <span class="btn-outline">LEARN MORE</span>
  </article>
</section>

<section class="abs info">
  <div class="feature">
    <h2>Presenting the Orbis System®</h2>
    <p>Orbis, Lumiscan® Refractive Analysis, is a revolutionary diagnostic device with Lumiscan technology that is designed to take intraoperative wavefront aberrometry to a higher level of performance. The Lumiscan technology has a precise light source and optics, the assurance of a live display of the eye, a convenient system-aligned, on-demand reticle and optimized algorithms to guide every refractive decision you make for your cataract patients.</p>
    <p class="more">See the Unique Benefits of the <span>Orbis System</span> &gt;</p>
  </div>
  <div class="appt">
    <h2>Appointment Request Form</h2>
    <form>
      <div class="field">Name</div>
      <div class="field">Phone</div>
      <div class="field">Date<span class="cal"></span></div>
      <div class="types">Type : <span><i></i>Eye Doctoe</span><span><i></i>Cataract</span></div>
      <span class="btn-submit">Submit</span>
    </form>
  </div>
</section>

<footer class="abs footer">
  <div class="footer-heads">
    <h4 style="left:116px">Testimonials</h4>
    <h4 style="left:277px">Navigation</h4>
    <h4 style="left:439px">Locations</h4>
    <h4 style="left:602px">Contact Us</h4>
  </div>
  <div class="col" style="left:116px;width:148px">
    <p>"After my cataract surgery...it was absolutely phenominal. My eyesight was restored back to normal. It's been nine years (since my cataract surgery), and I haven't worn glasses ever since. It was so comfortable, there was no pain involved."</p>
    <p style="margin-top:13px">— Daniel R.<br>Sterling Heights, Michigan</p>
  </div>
  <ul class="col links" style="left:277px">
    <li>&gt; Home</li><li>&gt; Appointment Request</li><li>&gt; Our Practice</li><li>&gt; Resources</li><li>&gt; Locations</li><li style="border:0">&gt; Contact</li>
  </ul>
  <div class="col" style="left:440px">
    <p>Visit us at any of our convenient locations!</p>
    <div class="map" role="img" aria-label="Map of Michigan office locations"><div></div></div>
  </div>
  <div class="col phones" style="left:604px">
    <ul class="links" style="width:150px"><li>&gt; Schedule an appointment</li><li style="border:0">&gt; Go to our contact page</li></ul>
    <p style="margin-top:8px">Michigan : (555) 014-2270</p>
    <p>Sterling Heights : (555) 014-2270</p>
    <p>Chesterfield&nbsp; : (555) 014-3310</p>
    <p>Cosmetic Surgery&nbsp; : (555) 014-2270</p>
  </div>
  <div class="footer-rule"></div>
  <p class="copyright">Copyright © 2011 Clearvale Optic Institute. All rights reserved.</p>
  <p class="backtop">back to top</p>
  <p class="about">Clearvale Optic Institute offers patient a variety of Ophthalmology, Refractive &amp; Cosmetic Services including, LASIK surgery, Eye Exams, Glaucoma Diagnosis &amp; Treatment, Cataract Surgery, Intercoular Lens Placement (IOL's), Treatment for Diabetic Retinopathy, Retinal Surgery, Treatment for Macular Degeration, Corneal Transplants, Skin Toning, Skin Tightening, Contour Therapy, Dermal Fillers &amp; Eye Lid Surgery. Serving patients in the Detroit Michigan area including, Sterling Heights &amp; Chesterfield Township.</p>
</footer>

</body>
</html>
```